quarry-mosaic artisans and studio

I need a web design for my company we offer counter tops. tile for floors,showers,kitchen backsplashes and more also need a place where the client
can write reviews

```html
<!DOCTYPE html>
<html lang="en">
<head>
<meta charset="utf-8">
<title>Quarry-Mosaic Artisans</title>
<link href="https://fonts.googleapis.com/css2?family=Open+Sans:wght@400;700&family=Roboto:wght@400;500&family=Roboto+Slab:wght@500&display=swap" rel="stylesheet">
<style>
:root{
  --red:#e8192c;
  --ink:#1a1a1a;
  --text:#555;
  --nav:#2c2c2c;
  --teal:#1b7a9c;
  --soft:#f4f4f4;
  --band:#1c1c1c;
  --foot:#222;
  --white:#fff;
  --blue:#4a86c8;
}
*{margin:0;padding:0;box-sizing:border-box}
html,body{width:947px;height:1200px;overflow:hidden;background:var(--white)}
body{position:relative;font-family:Arial,Helvetica,sans-serif;color:var(--ink)}
.abs{position:absolute}
.top-rule{left:0;top:0;width:947px;height:4px;background:var(--red)}
.brand{left:158px;top:22px;font-family:'Open Sans',sans-serif;font-weight:700;font-size:22px;color:var(--red);letter-spacing:-.2px}
.search{left:632px;top:23px;width:157px;height:24px;border:1px solid #ccc;box-shadow:0 1px 2px rgba(0,0,0,.15);font-size:7.5px;color:#999;padding:8px 0 0 12px}
.search svg{position:absolute;right:9px;top:6px}
.nav{left:0;top:66px;width:947px;height:44px;background:var(--nav);border-bottom:2px solid var(--red)}
.nav a{position:absolute;top:0;height:44px;line-height:44px;font-size:8px;color:var(--white);text-decoration:none}
.nav a.active{background:var(--red);width:102px;text-align:center;left:158px}
.hero{left:0;top:112px;width:947px;height:321px;background:linear-gradient(180deg,#5a3a2a 0%,#7a5038 35%,#cdb8a0 60%,#b49a80 100%)}
.hero-shade{left:0;top:112px;width:947px;height:34px;background:rgba(90,90,90,.55)}
.dots{left:464px;top:418px;display:flex;gap:5px}
.dots span{width:6px;height:6px;border-radius:50%;background:#222}
.dots span.on{background:var(--white);border:1.5px solid #2aa8c8}
.welcome{left:0;top:448px;width:947px;text-align:center;font-size:14.5px;font-weight:700;font-family:Roboto,Arial,sans-serif;font-weight:500}
.welcome em{font-style:normal;color:var(--red)}
.intro{left:160px;top:474px;width:622px;text-align:center;font-size:8px;line-height:15.2px;color:var(--text)}
.section-title{left:158px;top:555px;font-size:14.5px;color:var(--red);font-family:Roboto,Arial,sans-serif}
.card{top:591px;width:196px}
.card .photo{width:196px;height:128px}
.card h3{margin-top:12px;font-weight:400;font-size:11px;font-family:Roboto,Arial,sans-serif}
.card h3 em{font-style:normal;color:var(--red)}
.card p{margin-top:5px;font-size:7px;line-height:15px;color:var(--text)}
.card .more{font-size:8px;color:var(--ink)}
.card .more b{color:var(--red);font-weight:400}
.reviews{left:0;top:826px;width:947px;height:219px;background:var(--soft)}
.reviews h2{position:absolute;left:0;top:17px;width:947px;text-align:center;font-family:Roboto,Arial,sans-serif;font-weight:400;font-size:19px;color:var(--teal);letter-spacing:.5px}
.reviews .sub{position:absolute;left:0;top:40px;width:941px;text-align:center;font-size:7px;color:#444}
.quote{position:absolute;left:224px;top:78px;width:512px;font-size:11.2px;line-height:19.2px;color:#666;letter-spacing:.5px}
.arrow-box{position:absolute;top:84px;width:19px;height:19px;border:1px solid var(--blue);background:var(--white)}
.arrow-box svg{position:absolute;left:5px;top:4px}
.author{position:absolute;left:402px;top:153px;width:142px;height:48px;border:1px solid var(--blue);background:var(--white)}
.author:before{content:"";position:absolute;left:67px;top:-4px;border:4px solid transparent;border-top:0;border-bottom-color:var(--blue)}
.avatar{position:absolute;left:7px;top:6px;width:35px;height:35px;background:linear-gradient(135deg,#e8c89a,#d9825a)}
.author .name{position:absolute;left:56px;top:13px;font-family:'Roboto Slab',serif;font-size:9px;color:#333}
.author .role{position:absolute;left:56px;top:27px;font-size:6.5px;color:#999}
.band{left:0;top:1045px;width:947px;height:73px;background:var(--band)}
.band .item{position:absolute;top:14px;width:120px;margin-left:-60px;text-align:center;color:var(--white);font-family:Roboto,Arial,sans-serif;font-size:11px}
.band svg{display:block;margin:0 auto 8px}
.footer{left:0;top:1118px;width:947px;height:82px;background:var(--foot)}
.footer .links{position:absolute;left:158px;top:24px;font-size:7.5px;color:var(--white)}
.footer .links b{font-weight:700}
.footer .copy{position:absolute;left:158px;top:43px;font-size:7.5px;color:var(--white)}
.social{position:absolute;top:20px;width:16px;height:16px;border-radius:50%;background:var(--white)}
</style>
</head>
<body>
<div class="abs top-rule"></div>
<div class="abs brand">Quarry-Mosaic Artisans</div>
<div class="abs search">Search
  <svg width="11" height="11" viewBox="0 0 11 11"><circle cx="4.6" cy="4.6" r="3.6" fill="none" stroke="#333" stroke-width="1.4"/><line x1="7.3" y1="7.3" x2="10" y2="10" stroke="#333" stroke-width="1.5"/></svg>
</div>

<nav class="abs nav">
  <a class="active" href="#">Home</a>
  <a style="left:266px" href="#">About Us</a>
  <a style="left:346px" href="#">Services</a>
  <a style="left:423px" href="#">Marbles Tiles</a>
  <a style="left:517px" href="#">Prices</a>
  <a style="left:586px" href="#">Gallery</a>
  <a style="left:658px" href="#">Contact Us</a>
</nav>

<div class="abs hero" role="img" aria-label="Kitchen with stone range hood, mosaic tile backsplash and granite countertop"></div>
<div class="abs hero-shade"></div>
<svg class="abs" style="left:48px;top:243px" width="16" height="22" viewBox="0 0 16 22"><polyline points="12,2 4,11 12,20" fill="none" stroke="#fff" stroke-width="4"/></svg>
<svg class="abs" style="left:886px;top:245px" width="16" height="22" viewBox="0 0 16 22"><polyline points="4,2 12,11 4,20" fill="none" stroke="#fff" stroke-width="4"/></svg>
<div class="abs dots"><span class="on"></span><span></span><span></span></div>

<h1 class="abs welcome"><em>Welcome To</em> Quarry-Mosaic Artisans</h1>
<p class="abs intro">Lorem ipsum dolor sit amet, consectetuer adipiscing elit, sed diam nonummy nibh euismod tincidunt ut laoreet dolore magna aliquam erat volutpat. Lorem ipsum dolor sit amet, consectetuer adipiscing elit, sed diam nonummy nibh euismod tincidunt ut laoreet dolore magna aliquam erat volutpat. Lorem ipsum dolor sit amet, consectetuer adipiscing elit, sed diam nonummy nibh euismod tincidunt ut laoreet dolore magna aliquam erat volutpat. Lorem ipsum dolor sit amet, consectetuer adipiscing elit, sed diam nonummy nibh euismod tincidunt ut laoreet dolore magna aliquam erat volutpat.</p>

<h2 class="abs section-title">Services</h2>

<article class="abs card" style="left:158px">
  <div class="photo" role="img" aria-label="Rough-edged stone counter top on a dark vanity" style="background:linear-gradient(180deg,#d8e2d6 0%,#c3cfbe 45%,#7a5a3e 60%,#2a2a2a 100%)"></div>
  <h3>Counter <em>Tops</em></h3>
  <p>Lorem ipsum dolor sit amet, consectetuer adipiscing elit, sed diam nonummy nibh euismod tincidunt ut laoreet dolore magna aliquam erat volutpat.<br><span class="more">Read more <b>+</b></span></p>
</article>
<article class="abs card" style="left:376px">
  <div class="photo" role="img" aria-label="Large slab of veined green marble for floor tiles" style="background:linear-gradient(135deg,#6f6a58,#4e5246 50%,#8a8470)"></div>
  <h3>Tile for <em>Floors</em></h3>
  <p>Lorem ipsum dolor sit amet, consectetuer adipiscing elit, sed diam nonummy nibh euismod tincidunt ut laoreet dolore magna aliquam erat volutpat.<br><span class="more">Read more <b>+</b></span></p>
</article>
<article class="abs card" style="left:593px">
  <div class="photo" role="img" aria-label="Bathroom vanity with beige stone top and backsplash" style="background:linear-gradient(180deg,#aab8bc 0%,#c9b28e 45%,#3a2a24 70%,#7a3e38 100%)"></div>
  <h3>kitchen <em>backsplashes</em></h3>
  <p>Lorem ipsum dolor sit amet, consectetuer adipiscing elit, sed diam nonummy nibh euismod tincidunt ut laoreet dolore magna aliquam erat volutpat.<br><span class="more">Read more <b>+</b></span></p>
</article>

<section class="abs reviews">
  <h2>Tetmonials</h2>
  <div class="sub">happy Client about us</div>
  <div class="arrow-box" style="left:167px"><svg width="8" height="10" viewBox="0 0 8 10"><polyline points="6,1 2,5 6,9" fill="none" stroke="#4a86c8" stroke-width="1.4"/></svg></div>
  <p class="quote">Lorem ipsum dolor sit amet, consectetur adipiscing elit. Nulla convallis egestas rhoncus. Donec facilisis fermentum sem, ac viverra ante luctus vel. Donec vel mauris quam. Aliquam pellentesque pellentesque turpis, ut bibendum sapien sollicitudin nec.</p>
  <div class="arrow-box" style="left:759px"><svg width="8" height="10" viewBox="0 0 8 10"><polyline points="2,1 6,5 2,9" fill="none" stroke="#4a86c8" stroke-width="1.4"/></svg></div>
  <div class="author">
    <div class="avatar" role="img" aria-label="Client portrait"></div>
    <div class="name">Elena Varga</div>
    <div class="role">senior designer</div>
  </div>
</section>

<div class="abs band">
  <div class="item" style="left:184px">
    <svg width="16" height="16" viewBox="0 0 16 16"><path d="M3 1l3 0 1.5 4-2 1.5c1 2 2.5 3.5 4 4l1.5-2 4 1.5 0 3c-7 1-13-5-12-12z" fill="#fff"/></svg>Talk to u</div>
  <div class="item" style="left:369px">
    <svg width="19" height="16" viewBox="0 0 19 16"><ellipse cx="9.5" cy="7" rx="9" ry="6.5" fill="#fff"/><path d="M4 11l-1 5 5-3z" fill="#fff"/></svg>Live Chat</div>
  <div class="item" style="left:553px">
    <svg width="19" height="16" viewBox="0 0 19 16"><rect x="0" y="2" width="19" height="13" fill="#fff"/><polyline points="0,3 9.5,10 19,3" fill="none" stroke="#1c1c1c" stroke-width="1.5"/></svg>Email Us</div>
  <div class="item" style="left:738px">
    <svg width="17" height="16" viewBox="0 0 17 16"><rect x="0" y="7" width="4" height="9" fill="#fff"/><path d="M5 7l3-6c2 0 2 2 1.5 4h5.5c1.5 0 2 1.5 1.5 2.5l-2 7.5c-.3 1-1 1-1.5 1h-8z" fill="#fff"/></svg>Good Support</div>
</div>

<footer class="abs footer">
  <div class="links">Home &nbsp;|&nbsp; About Us &nbsp;|&nbsp; Services &nbsp;|&nbsp; <b>News/Blog</b> &nbsp;|&nbsp; <b>Contact Us</b></div>
  <div class="copy">Copyright Quarry-Mosaic Artisans.&nbsp; All rights reserved.</div>
  <span class="social" style="left:732px"></span>
  <span class="social" style="left:753px"></span>
  <span class="social" style="left:774px"></span>
</footer>
</body>
</html>
```